Hot sauce company needs a logo and label design- simple, clean & fresh

Wendel T's a hot pepper sauce company based on the edge of London needs a logo and label design .
The sauces are handmade in small batches with natural ingredients , no added sugars or extracts and so we would like a clean fresh label to reflect this - avoiding all the macho devil and flames novelty stuff.
At present there are four sauces - Jalapeno ,Chipotle,Habanero and Reaper we would like to have one Wendel T's label with the name of the sauce being changeable allowing us to react to what ingredients are available .
Updates

Project Deadline Extended
Reason: Hi Guys I have received a few requests to extend the deadline on the project and so I am thanks Wendel T's

Target Market(s)

people who care what they eat

Industry/Entity Type

Food Store

Logo Text

Wendel T's handmade hot sauce

Requirements
Must have
• Wendel T's handmade hot sauce - or the logo
• the name of the sauce ie jalapeno
• no added sugars
Nice to have
• handmade
• small batch
Should not have
• cartoon men with smoke coming out of their ears
• devils and the flames of hell

```html
<!DOCTYPE html>
<html lang="en">
<head>
<meta charset="utf-8">
<title>Wendel T's Jalapeno Label</title>
<link rel="stylesheet" href="https://fonts.googleapis.com/css2?family=Cinzel:wght@900&family=Barlow+Condensed:wght@400&display=swap">
<style>
  :root {
    --label-red: #b71f27;
    --label-black: #0c0c0c;
    --paper: #ffffff;
    --ink: #1a1a1a;
  }
  html, body {
    margin: 0;
    padding: 0;
    width: 1200px;
    height: 864px;
    overflow: hidden;
    background: var(--paper);
  }
  .canvas {
    position: relative;
    width: 1200px;
    height: 864px;
  }
  .label-front {
    position: absolute;
    left: 0;
    top: 0;
    width: 856px;
    height: 862px;
    border-right: 2px solid var(--label-black);
    border-bottom: 2px solid var(--label-black);
    box-sizing: border-box;
  }
  .band-top {
    position: absolute;
    left: 0; top: 0;
    width: 100%;
    height: 47px;
    background: var(--label-black);
  }
  .brand-field {
    position: absolute;
    left: 0; top: 55px;
    width: 100%;
    height: 697px;
    background: var(--label-red);
  }
  .brand-line {
    position: absolute;
    left: 0;
    width: 100%;
    margin: 0;
    text-align: center;
    font-family: "Cinzel", serif;
    font-weight: 900;
    line-height: 1;
    color: var(--paper);
  }
  .brand-name {
    top: 110px;
    font-size: 104px;
  }
  .brand-made {
    top: 240px;
    font-size: 56px;
    letter-spacing: 6px;
  }
  .brand-mark {
    position: absolute;
    left: 338px;
    top: 330px;
    width: 176px;
    height: 176px;
    border-radius: 50%;
    background: var(--label-black);
  }
  .brand-sauce {
    top: 540px;
    font-size: 68px;
  }
  .band-flavour {
    position: absolute;
    left: 0; top: 761px;
    width: 100%;
    height: 99px;
    background: var(--label-black);
    display: flex;
    align-items: center;
    justify-content: center;
  }
  .flavour-name {
    margin: 0;
    font-family: "Cinzel", serif;
    font-weight: 900;
    font-size: 44px;
    letter-spacing: 1px;
    color: var(--paper);
  }
  .label-back {
    position: absolute;
    left: 884px;
    top: 62px;
    width: 307px;
    margin: 0;
    font-family: "Barlow Condensed", sans-serif;
    font-weight: 400;
    font-size: 22px;
    line-height: 36.5px;
    color: var(--ink);
  }
  .label-back span {
    display: block;
    white-space: nowrap;
    text-align: justify;
    text-align-last: justify;
  }
</style>
</head>
<body>
<div class="canvas">
  <section class="label-front">
    <div class="band-top"></div>
    <div class="brand-field">
      <h1 class="brand-line brand-name">Wendel T's</h1>
      <p class="brand-line brand-made">HAND MADE</p>
      <span class="brand-mark"></span>
      <p class="brand-line brand-sauce">Hot Sauce</p>
    </div>
    <div class="band-flavour">
      <h2 class="flavour-name">JALAPENO</h2>
    </div>
  </section>
  <p class="label-back">
    <span>At vero eos et accusamus et iusto</span>
    <span>odio dignissimos ducimus qui</span>
    <span>bland itiis praesent ium volupt</span>
    <span>atum deleniti atque corrupti quos</span>
    <span>dolores et quas molestias except</span>
    <span>uri sint occaecati cupiditate non</span>
    <span>provident, similique sunt in culpa</span>
    <span>qui officia deserunt mollitia</span>
    <span>animi, id est laborum et dolorum</span>
    <span>fuga. Et harum quidem rerum</span>
    <span>facilis est et expedita distinctio.</span>
    <span>Nam libero tempore, cum soluta</span>
    <span>nobis est eligendi optio cumque</span>
    <span>nihil imped it quo minus id quod</span>
    <span>maxime placeat facere possimus,</span>
    <span>omnis voluptas assumenda est,</span>
    <span>omnis dolor repellendus.</span>
    <span>Temporibus autem quibusdam et</span>
    <span>aut officiis debitis aut rerum</span>
    <span>necessitatibus saepe eveniet ut</span>
    <span>et voluptates repudiandae sint et</span>
  </p>
</div>
</body>
</html>
```